Web landing page design

- Create a Web Design (Uncoded - PSD layout only)

We need a single web page design to promote our service. This page will
acts as a landing page for users and also be utilized in social media
advertising. Please provide us with a cutting edge design. I have attached
a link for what the company is about. In essence we are a photo checking
service which reviews photos for retailers, hotels abd car dealerships to
check everything is good after a service has been performed. Whether it be
a new promotion, cleaning or just checking prices. I am looking for a
design to say that we do many photos and at a very cost effective price
(team based in Mexico)

Link: https://slidewharf.example/view/qT4nRz8LmXcV2pKdHs0w/
*Deadline*
5 days
*Updates*

- The Start Here box needs to look like this:

-Start Here (heading)
-A box for email addresses to be entered
-Then a check box with "Yes, I have read and agree to the Privacy Policy
and agree to receive email marketing from Snapora88'
-A submit button

All of this information needs to be in one box please. And please feel
free to contact me if you have any questions about this.

*Target Market(s)*
Retail business, Merchandising companies, Rental property owners, Car
dealers
Updates

Please can you submit entries. I am just looking for a tidy to a presentation already created. Just needs design touches.

Target Market(s)

Ability for audience to understand concept quickly
Benefits to why to use the product stand out
Technology driven approach

Industry/Entity Type

Retail

Number of Pages Required

1 page

Colors
0792cd

Requirements
Must have
• Clean and modern design

```html
<!DOCTYPE html>
<html lang="en">
<head>
<meta charset="utf-8">
<title>Snapora88 – Transform Retail Execution</title>
<link href="https://fonts.googleapis.com/css2?family=Roboto:wght@300;400;500;700&display=swap" rel="stylesheet">
<style>
:root{
  --brand:#0792cd;
  --brand-dark:#0678ab;
  --ink:#1b1b1b;
  --text:#333;
  --muted:#8a8a8a;
  --white:#fff;
  --dark:#2a2a2a;
  --line:#e2e2e2;
}
*{box-sizing:border-box;margin:0;padding:0}
html,body{width:711px;height:1200px;overflow:hidden}
body{font-family:"Roboto",Arial,sans-serif;color:var(--text);background:var(--white);position:relative}
.abs{position:absolute}

/* hero */
.hero{left:0;top:0;width:711px;height:270px;background:linear-gradient(160deg,#5f7d4e 0%,#8fa772 40%,#4e6a3f 75%,#7a9460 100%)}
.hero-person{left:100px;top:20px;width:290px;height:250px;border-radius:40% 40% 10% 10%;background:linear-gradient(180deg,#c9bfa8,#e4e2dc 50%,#bdb8ae)}
.logo{left:104px;top:12px;display:flex;align-items:center;gap:4px;color:var(--brand);font-weight:500;font-size:15px}
.logo-dot{width:12px;height:12px;border-radius:50%;background:var(--brand)}
.nav{left:451px;top:17px;display:flex;gap:14px;font-size:6.5px;font-weight:500;letter-spacing:.4px;color:var(--white)}
.hero-title{left:300px;top:116px;width:336px;text-align:center;color:var(--white);font-size:23px;line-height:24px;font-weight:300}
.hero-title b{font-weight:500}
.hero-tick{left:454px;top:174px}

/* start here */
.start{left:0;top:260px;width:711px;height:90px;background:linear-gradient(180deg,rgba(7,146,205,.88),var(--brand))}
.start h2{position:absolute;left:122px;top:29px;color:var(--white);font-size:19px;font-weight:500}
.start .email{position:absolute;left:226px;top:27px;width:231px;height:25px;background:var(--white);font-size:6px;color:var(--muted);padding:8px 7px}
.start .submit{position:absolute;left:463px;top:27px;width:105px;height:25px;background:#0b0b0b;color:var(--white);font-size:7px;font-weight:700;text-align:center;line-height:25px;letter-spacing:.3px}
.start .consent{position:absolute;left:226px;top:57px;display:flex;gap:6px;color:var(--white);font-size:5px;line-height:6.5px;width:210px}
.start .box{width:7px;height:7px;background:var(--white);flex:none;margin-top:1px}

/* stats */
.stats{left:0;top:350px;width:711px;height:128px;background:#f7f7f7}
.stat{position:absolute;top:16px;width:92px;height:92px;border-radius:50%;background:var(--white);box-shadow:0 0 0 5px #eef3f6;text-align:center;padding-top:26px}
.stat strong{display:block;color:var(--brand);font-size:18px;font-weight:400}
.stat span{display:block;font-size:6.5px;color:var(--ink);line-height:8px;margin-top:2px}
.stat.featured{background:var(--brand);box-shadow:0 0 0 5px #d5ebf6}
.stat.featured strong,.stat.featured span{color:var(--white)}
.stats svg{position:absolute;left:0;top:0}

/* results */
.results-bg{left:0;top:478px;width:711px;height:294px;background:linear-gradient(120deg,#3a3c44 0%,#7a6a58 35%,#4a4e5a 70%,#2c2e36 100%)}
.results-label{left:102px;top:526px;width:118px;height:211px;background:#111;color:var(--white)}
.results-label h2{position:absolute;left:0;top:84px;width:118px;text-align:center;font-size:23px;line-height:22px;font-weight:300}
.results-label h2 b{font-weight:700}
.results-label .notch{position:absolute;right:-14px;top:97px;width:0;height:0;border-top:14px solid transparent;border-bottom:14px solid transparent;border-left:14px solid #111}
.results-panel{left:220px;top:526px;width:388px;height:211px;background:var(--white)}
.case{position:absolute;text-align:center;width:80px;font-size:5.5px;color:var(--ink);line-height:7px}
.case .brand{font-size:8px;font-weight:700;color:#3a3a3a;height:10px}
.case .cat{font-weight:700;color:#1e3b5a;font-size:5px;margin:1px 0 2px}
.case .shot{width:56px;height:39px;margin:0 auto 3px}

/* how */
.how-bg{left:0;top:772px;width:711px;height:310px;background:linear-gradient(90deg,#222 0%,#3a3a3a 50%,#262626 100%)}
.how-label{left:102px;top:813px;width:116px;height:236px;background:var(--brand);color:var(--white)}
.how-label h2{position:absolute;left:0;top:100px;width:116px;text-align:center;font-size:22px;line-height:22px;font-weight:300}
.how-label h2 b{font-weight:700}
.step{position:absolute;background:var(--white);font-size:9.5px;line-height:13px;color:var(--ink);padding:5px 8px}
.step em{font-style:normal;color:var(--brand)}
.step-list{position:absolute;left:100px;top:34px;list-style:none;font-size:6px;line-height:9px;z-index:2}
.shot-fill{position:absolute}
.screen{position:absolute;background:#222;border-radius:2px}
.screen i{position:absolute;inset:3px;background:linear-gradient(180deg,#e8ecef,#f8f8f8)}

/* subscribe */
.subscribe{left:0;top:1082px;width:711px;height:36px;background:var(--brand)}
.subscribe h3{position:absolute;left:104px;top:10px;color:var(--white);font-size:12.5px;font-weight:400}
.subscribe h3 b{font-weight:700}
.subscribe .email{position:absolute;left:346px;top:6px;width:181px;height:23px;background:var(--white);font-size:5.5px;color:var(--muted);padding:8px 6px}
.subscribe .btn{position:absolute;left:534px;top:6px;width:73px;height:23px;background:#0b0b0b;color:var(--white);font-size:6.5px;font-weight:700;text-align:center;line-height:23px}

/* footer */
.social{left:317px;top:1127px;display:flex;gap:6px}
.social span{width:15px;height:15px;border-radius:50%;background:#d4d4d4}
.footer-rule{left:138px;top:1153px;width:435px;height:1px;background:var(--line)}
.footer-links{left:0;top:1165px;width:711px;text-align:center;font-size:5.5px;color:var(--muted);word-spacing:2px}
.footer-links span{margin:0 4px}
.copyright{top:1176px}
</style>
</head>
<body>

<!-- Hero -->
<div class="abs hero" role="img" aria-label="Man in a straw hat using a tablet outdoors above green hills"></div>
<div class="abs hero-person" role="img" aria-label="Seated man in white shirt holding a tablet"></div>
<div class="abs logo"><span class="logo-dot"></span>Snapora88</div>
<nav class="abs nav"><span>ABOUT US</span><span>RESULTS</span><span>HOW</span><span>FREE TRIAL</span></nav>
<h1 class="abs hero-title">Transform <b>Retail Execution</b><br><b>With a Simple Photo</b></h1>
<svg class="abs hero-tick" width="28" height="28" viewBox="0 0 28 28"><circle cx="14" cy="14" r="14" fill="#fff"/><path d="M8 14.5l4 4 8-8" stroke="#0792cd" stroke-width="3" fill="none" stroke-linecap="round" stroke-linejoin="round"/></svg>

<!-- Start here -->
<section class="abs start">
  <h2>Start Here</h2>
  <div class="email">Email address</div>
  <div class="submit">SUBMIT NOW ›</div>
  <label class="consent"><span class="box"></span><span>Yes, I have read and agree to the Privacy Policy and agree to receive email marketing from Snapora88</span></label>
</section>

<!-- Stats -->
<section class="abs stats">
  <svg width="711" height="128"><g stroke="#c8c8c8" stroke-dasharray="2 2" fill="none"><path d="M197 66 Q215 62 232 64"/><path d="M334 44 Q352 38 370 44"/><path d="M470 66 Q488 70 506 64"/></g></svg>
  <div class="stat" style="left:104px"><strong>2.2m</strong><span>Photos reviewed<br>last year</span></div>
  <div class="stat" style="left:242px"><strong>5p</strong><span>From per photo<br>reviewed</span></div>
  <div class="stat featured" style="left:378px"><strong>97.2%</strong><span>Average<br>compliance</span></div>
  <div class="stat" style="left:516px"><strong>3-8%</strong><span>Sales increase</span></div>
</section>

<!-- Results -->
<div class="abs results-bg" role="img" aria-label="Blurred photo of a woman working at a laptop in a warm-lit room"></div>
<div class="abs results-label">
  <svg class="abs" style="left:45px;top:50px" width="28" height="28" viewBox="0 0 28 28"><circle cx="14" cy="14" r="14" fill="#fff"/><path d="M8 14.5l4 4 8-8" stroke="#111" stroke-width="3" fill="none" stroke-linecap="round" stroke-linejoin="round"/></svg>
  <h2>Our<br><b>Results</b></h2>
  <span class="notch"></span>
</div>
<div class="abs results-panel">
  <div class="case" style="left:32px;top:28px"><div class="brand">Grenwick</div><div class="cat">Poster Set Up</div><div class="shot" role="img" aria-label="Store aisle with promotional posters" style="background:linear-gradient(180deg,#cfd8de,#8e9aa3)"></div>+40% compliance<br>within 2 cycles</div>
  <div class="case" style="left:114px;top:28px"><div class="brand">Hollbury</div><div class="cat">Clothing Events</div><div class="shot" role="img" aria-label="Clothing rails in a supermarket" style="background:linear-gradient(180deg,#b7bcc6,#5a5f6e)"></div>+60% compliance<br>within 3 cycles</div>
  <div class="case" style="left:192px;top:28px"><div class="brand">Parlo</div><div class="cat">Range Change</div><div class="shot" role="img" aria-label="Homeware shelf display" style="background:linear-gradient(180deg,#c6bdb4,#6d625b)"></div>+8% Sales<br>vs. control group</div>
  <div class="case" style="left:274px;top:28px"><div class="brand">Cardwell</div><div class="cat">Seqyebce Compliance</div><div class="shot" role="img" aria-label="Gift card display rack" style="width:76px;height:102px;background:linear-gradient(180deg,#6a8fb0,#c25a4f 50%,#3f6f4a)"></div></div>
  <div class="case" style="left:32px;top:124px"><div class="cat">Hotel Rooms</div><div class="shot" role="img" aria-label="Hotel bedroom" style="background:linear-gradient(180deg,#8a7c6c,#4a3e34)"></div></div>
  <div class="case" style="left:114px;top:124px"><div class="cat">Car Showroom</div><div class="shot" role="img" aria-label="Car showroom interior" style="background:linear-gradient(180deg,#9aa0a6,#2f3338)"></div></div>
  <div class="case" style="left:192px;top:124px"><div class="cat">Pricing</div><div class="shot" role="img" aria-label="Shelf price labels" style="background:#aab0b5"></div></div>
</div>

<!-- How -->
<div class="abs how-bg" role="img" aria-label="Dark photo of a man with glasses at a desk"></div>
<div class="abs how-label">
  <svg class="abs" style="left:44px;top:66px" width="28" height="28" viewBox="0 0 28 28"><circle cx="14" cy="14" r="14" fill="#fff"/><path d="M8 14.5l4 4 8-8" stroke="#0792cd" stroke-width="3" fill="none" stroke-linecap="round" stroke-linejoin="round"/></svg>
  <h2>How we<br><b>drive<br>sales</b></h2>
</div>
<div class="step" style="left:218px;top:813px;width:92px;height:116px;padding:5px 10px">1. <em>We</em> prepare the brief and digital survey
  <div class="shot-fill" role="img" aria-label="Hand holding a smartphone" style="left:4px;top:64px;width:50px;height:44px;border-radius:8px;background:linear-gradient(135deg,#e9c9ae,#222 55%)"></div></div>
<div class="shot-fill" role="img" aria-label="Hands photographing a shelf with a phone" style="left:310px;top:813px;width:128px;height:116px;background:linear-gradient(180deg,#6a6660,#a49a8e 60%,#d8c1a6)"></div>
<div class="abs" style="left:344px;top:880px;width:62px;height:34px;background:rgba(255,255,255,.85);border-radius:4px;font-size:9.5px;line-height:12px;padding:5px 6px;color:var(--ink)">2. <span style="color:var(--brand)">We</span> take photo's</div>
<div class="step" style="left:438px;top:813px;width:170px;height:116px">3. <em>We</em> track each activity
  <div class="screen" style="left:10px;top:26px;width:76px;height:54px"><i></i></div>
  <div class="screen" style="left:62px;top:66px;width:56px;height:38px"><i></i></div>
  <ul class="step-list"><li>• Quick Stats</li><li>• SMS Alerts</li><li>• Real-Time Updates</li></ul></div>
<div class="step" style="left:438px;top:929px;width:170px;height:120px;background:#666;color:var(--white)">5. <em>We</em> turn photo's into insights &amp; actions
  <div class="screen" style="left:34px;top:42px;width:84px;height:56px"><i></i></div>
  <div class="screen" style="left:104px;top:50px;width:44px;height:56px;border-radius:4px"><i></i></div>
  <div class="screen" style="left:40px;top:86px;width:80px;height:30px;border-radius:4px"><i></i></div></div>
<div class="step" style="left:218px;top:929px;width:220px;height:120px">4. <em>We</em> send corrective actions to each location.
  <div style="font-size:7px;font-style:italic;text-align:center;margin-top:1px">Within <em style="font-weight:700">30 minutes</em></div>
  <div class="screen" style="left:47px;top:40px;width:68px;height:48px"><i></i></div>
  <div class="screen" style="left:148px;top:38px;width:30px;height:56px;background:#ddd;border-radius:5px"><i style="background:#fff"></i></div></div>

<!-- Subscribe -->
<section class="abs subscribe">
  <h3><b>SUBSCRIBE NOW,</b> AND JOIN THE FAMILY!</h3>
  <div class="email">Enter your email address</div>
  <div class="btn">SUBSCRIBE NOW</div>
</section>

<!-- Footer -->
<div class="abs social"><span></span><span></span><span></span><span></span></div>
<div class="abs footer-rule"></div>
<div class="abs footer-links"><span>About Us</span><span>Results</span><span>How</span><span>Free Trial</span></div>
<div class="abs footer-links copyright"><span>© 2018 Snapora88. All rights reserved -</span><span>Privacy Policy</span><span>Terms of Service</span><span>Cookie Consent</span></div>

</body>
</html>
```